Seeking for catalogue design -for Event Mgmt company

Need to be creative and striking and images to be more enhanced.
The items in the catalogue have to be layout well and easy to read.
Cover and background of catalogue needs to be striking but not overpowering the items.
Catologue needs to be able to put up on website and able to read on mobile.
Font used must be easily readable and not too small.

Target Market(s)

Business and Public Sectors

Industry/Entity Type

Event Planning

Colors

Designer to choose colors to be used in the design.

Requirements
Must have
• Not too many colors but must be creative
Nice to have
• See that the images of items in catalogue have better layout
Should not have
• Not to be so messy

```html
<!DOCTYPE html>
<html lang="en">
<head>
<meta charset="utf-8">
<title>Carnival Game Stalls</title>
<link href="https://fonts.googleapis.com/css2?family=Dosis:wght@300;400;700&display=swap" rel="stylesheet">
<style>
:root{
  --page:#b3b3b5;
  --circle-light:#d3d3d5;
  --accent-yellow:#fdca0a;
  --card:#d9d9d9;
  --title-ink:#3a3a3a;
  --body-ink:#555;
  --item-red:#e2102d;
}
*{margin:0;padding:0;box-sizing:border-box}
html,body{width:849px;height:1200px;overflow:hidden;background:var(--page)}
.catalogue-page{position:relative;width:849px;height:1200px;overflow:hidden;background:var(--page);font-family:'Dosis',sans-serif}
.decor{position:absolute;inset:0;width:849px;height:1200px}
.page-title{position:absolute;right:86px;top:40px;text-align:right;font-weight:300;font-size:61px;line-height:82px;color:var(--title-ink);letter-spacing:.5px}
.stall-card{position:absolute;width:312px;height:207px;background:var(--card);display:flex;padding:12px 14px}
.stall-photo{width:138px;height:183px;flex:none}
.stall-info{margin-left:14px;padding-top:4px}
.stall-name{font-weight:700;font-size:17px;color:var(--item-red);line-height:22px;margin-bottom:3px}
.stall-info p{font-size:14px;line-height:23px;color:var(--body-ink);font-weight:400}
.col-left{left:100px}.col-right{left:452px}
.row-1{top:235px}.row-2{top:462px}.row-3{top:688px}.row-4{top:910px}
</style>
</head>
<body>
<div class="catalogue-page">
  <svg class="decor" viewBox="0 0 849 1200" aria-hidden="true">
    <circle cx="45" cy="0" r="225" fill="var(--circle-light)"/>
    <circle cx="0" cy="307" r="82" fill="var(--accent-yellow)"/>
    <circle cx="710" cy="1190" r="285" fill="var(--accent-yellow)"/>
  </svg>

  <h1 class="page-title">Carnival<br>Game Stalls</h1>

  <article class="stall-card col-left row-1">
    <div class="stall-photo" role="img" aria-label="Finish the race game stall photo" style="background:linear-gradient(160deg,#2a2a2a,#111 60%,#1d2a4a)"></div>
    <div class="stall-info"><h2 class="stall-name">Finish The Race</h2><p>0.93m by 0.93m</p><p>$145/stall (Min 3 stalls)</p><p>Require 1x Table</p><p>Subsequent day: $70</p></div>
  </article>

  <article class="stall-card col-right row-1">
    <div class="stall-photo" role="img" aria-label="Archery game stall photo" style="background:linear-gradient(180deg,#3b6a4a,#c56a2a 30%,#c76d2c 70%,#5b8b6a)"></div>
    <div class="stall-info"><h2 class="stall-name">Archery Game</h2><p>0.93m by 0.93m</p><p>$145/stall (Min 3 stalls)</p><p>Require 1x Table</p><p>Subsequent day: $70</p></div>
  </article>

  <article class="stall-card col-left row-2">
    <div class="stall-photo" role="img" aria-label="Dart game stall photo" style="background:linear-gradient(180deg,#2b3560,#2a3866 60%,#e5421c 70%,#ef4a1d)"></div>
    <div class="stall-info"><h2 class="stall-name">Dart Game</h2><p>0.93m by 0.93m</p><p>$145/stall (Min 3 stalls)</p><p>Require 1x Table</p><p>Subsequent day: $70</p></div>
  </article>

  <article class="stall-card col-right row-2">
    <div class="stall-photo" role="img" aria-label="Basketball game stall photo" style="background:linear-gradient(180deg,#ef4c22,#e0451c)"></div>
    <div class="stall-info"><h2 class="stall-name">Basketball Game</h2><p>0.93m by 0.93m</p><p>$145/stall (Min 3 stalls)</p><p>Require 1x Table</p><p>Subsequent day: $70</p></div>
  </article>

  <article class="stall-card col-left row-3">
    <div class="stall-photo" role="img" aria-label="Fetch game stall photo" style="background:linear-gradient(180deg,#8fd0ea,#d8eef6 55%,#f2f2f2)"></div>
    <div class="stall-info"><h2 class="stall-name">Fetch Game</h2><p>0.93m by 0.93m</p><p>$145/stall (Min 3 stalls)</p><p>Require 1x Table</p><p>Subsequent day: $70</p></div>
  </article>

  <article class="stall-card col-right row-3">
    <div class="stall-photo" role="img" aria-label="Coin toss stall photo" style="background:linear-gradient(180deg,#3aa6d8,#f6c640 45%,#1d8fc9 70%,#1b1b1b)"></div>
    <div class="stall-info"><h2 class="stall-name">Coin Toss</h2><p>0.93m by 0.93m</p><p>$145/stall (Min 3 stalls)</p><p>Require 1x Table</p><p>Subsequent day: $70</p></div>
  </article>

  <article class="stall-card col-left row-4">
    <div class="stall-photo" role="img" aria-label="Tic tac toe stall photo" style="background:linear-gradient(180deg,#2d7fc7,#5fb0e0 40%,#3f9b3a 70%,#d8432a)"></div>
    <div class="stall-info"><h2 class="stall-name">Tic Tac Toe</h2><p>0.93m by 0.93m</p><p>$145/stall (Min 3 stalls)</p><p>Require 1x Table</p><p>Subsequent day: $70</p></div>
  </article>

  <article class="stall-card col-right row-4">
    <div class="stall-photo" role="img" aria-label="Baseball game stall photo" style="background:linear-gradient(180deg,#9cc9e6,#3e8a3f 30%,#4a9a45 65%,#e8e8e8)"></div>
    <div class="stall-info"><h2 class="stall-name">Baseball Game</h2><p>0.93m by 0.93m</p><p>$145/stall (Min 3 stalls)</p><p>Require 1x Table</p><p>Subsequent day: $70</p></div>
  </article>
</div>
</body>
</html>
```